SunHaven Webpage for Integrative and Holistic Psychiatric Practice

We need a webpage designed for a medical practice that focuses on integrative and holistic psychiatry. We focus on providing care to mothers and families. The name of the company is Sun Haven, incorporated, A Professional Medical Corporation.

We'd like the color palette to be earthy/natural with the same look and feel as our logo that's attached. We're not set on anything, so feel free to have fun with the palette. We just want it to be warm and inviting in particular for Moms!

We'd like to have our logo in the top left with links below it either centered or to the right. We really like websites like http://www.brightvalecare.example/home.html and http://www.marlowridgeclinic.example/site/ to give you an idea of what we're looking for.

For links, we're looking for the following. Dummy text is fine, we're still getting content together:

* Home
* About Us - this page would have headings for Directions, Staff, Appointment Scheduling
* Services Provided - headings for 8 different services
* Patient Resources - headings for Patient Forms, Fees, Articles
* FAQ
* Contact Us

The webpage will be hosted as an Office 365 Public Website, so feel free to use whatever SharePoint integration you would like, but it's not necessary.

Thank you!

```html
<!DOCTYPE html>
<html lang="en">
<head>
<meta charset="utf-8">
<title>SunHaven — Integrative &amp; Holistic Psychiatry</title>
<link rel="stylesheet" href="https://fonts.googleapis.com/css2?family=Nothing+You+Could+Do&family=Mulish:wght@400;700&display=swap">
<style>
:root{
  --cream:#f3ead7;
  --cream-light:#f8f1e2;
  --brown:#5a2810;
  --brown-dark:#3f1a08;
  --green:#1e7a1e;
  --green-dark:#0f5c10;
  --green-title:#2b7a22;
  --text:#3a332b;
  --rule:#b08a64;
  --card:#ffffff;
}
*{box-sizing:border-box;margin:0;padding:0}
html,body{width:716px;height:1200px;overflow:hidden;background:var(--cream)}
body{font-family:"Mulish",Arial,sans-serif;color:var(--text)}
.page{position:relative;width:716px;height:1200px;overflow:hidden;background:linear-gradient(var(--cream-light),var(--cream))}
.script{font-family:"Nothing You Could Do",cursive}

.site-header{position:absolute;left:0;top:0;width:716px;height:55px}
.brand{position:absolute;left:54px;top:14px;display:flex;align-items:center;gap:7px;font-size:17px;color:var(--brown);font-weight:700}
.brand-dot{width:14px;height:14px;border-radius:50%;background:var(--green)}
.main-nav{position:absolute;right:58px;top:20px;display:flex;gap:30px;font-size:10.5px}
.main-nav a{color:var(--brown);text-decoration:none}
.main-nav a.current{color:var(--green)}

.hero{position:absolute;left:0;top:55px;width:716px;height:285px;
  background:radial-gradient(ellipse at 38% 30%,#fbf6c8 0%,#e4ec8a 25%,#a9c94a 55%,#6d9a2c 80%,#4d7420 100%)}

.hero-band{position:absolute;left:0;top:340px;width:716px;height:57px;background:var(--brown);border-top:2px dashed #7b4222;border-bottom:2px dashed #7b4222}
.band-arrow{position:absolute;top:21px}
.band-brand{position:absolute;left:104px;top:19px;display:flex;align-items:center;gap:5px;color:#fff;font-size:11px;font-weight:700;white-space:nowrap}
.band-brand .brand-dot{width:9px;height:9px;background:#fff}
.tagline{position:absolute;left:184px;top:18px;width:300px;font-size:11.5px;color:#fff;white-space:nowrap}
.pay-btn{position:absolute;left:495px;top:14px;width:144px;height:29px;background:var(--green);color:#fff;font-size:12px;text-align:center;line-height:30px;border-bottom:2px solid var(--green-dark);white-space:nowrap}

.card{position:absolute;top:428px;width:186px;height:240px;background:var(--card);box-shadow:0 1px 4px rgba(0,0,0,.18)}
.card-title{font-size:12px;color:var(--green-title);padding:10px 12px 0;height:32px;border-bottom:1px dashed #d6cbbb;white-space:nowrap}
.card-photo{margin:9px 9px 0;height:82px;border-radius:2px}
.card-text{font-size:6.4px;line-height:14.4px;padding:6px 9px 0}
.news-item{display:flex;gap:5px;padding:7px 8px 0}
.news-photo{width:66px;height:53px;flex:none}
.news-text{font-size:6.3px;line-height:10.6px}
.news-text b{font-weight:700}
.more-btn{display:block;margin:3px 8px 0 auto;width:44px;height:14px;background:var(--green);color:#fff;font-size:7px;text-align:center;line-height:15px;white-space:nowrap}

.section-title{position:absolute;font-size:12.5px;color:var(--green-title);white-space:nowrap}
.rule{position:absolute;height:3px;border-top:1px dashed var(--rule);border-bottom:1px solid var(--rule)}

.resource-photo{position:absolute;left:60px;top:740px;width:159px;height:119px;background:linear-gradient(135deg,#e8ecd2,#c6d48c 45%,#d9b89a 70%,#a7c06a)}
.resource-text{position:absolute;left:228px;top:738px;width:118px;font-size:6.6px;line-height:11.9px}

.service{position:absolute;left:363px;width:290px}
.service-icon{position:absolute;left:0;top:0;width:52px;height:52px;border-radius:50%;background:var(--green);border:2px solid #fff;box-shadow:0 0 0 1px var(--green)}
.service-body{position:absolute;left:68px;top:0;width:218px}
.service-title{font-size:10.5px;color:var(--brown);white-space:nowrap}
.service-text{font-size:6.6px;line-height:13.7px;margin-top:3px}

.map{position:absolute;left:60px;top:935px;width:591px;height:188px;border:3px solid #fff;box-shadow:0 1px 4px rgba(0,0,0,.2);
  background:linear-gradient(120deg,#eae6dc 0%,#e3ddd0 40%,#ecd6d6 48%,#e6e2d6 60%,#dfe4cf 100%)}
.contact-panel{position:absolute;left:457px;top:932px;width:148px;height:180px;background:rgba(20,110,15,.88);color:#fff;padding:20px 12px 0}
.contact-panel h3{font-family:"Nothing You Could Do",cursive;font-weight:400;font-size:12.5px;margin-bottom:12px}
.contact-panel p{font-size:7px;line-height:12px;white-space:nowrap}
.contact-panel .gap{margin-top:12px}

.site-footer{position:absolute;left:0;top:1152px;width:716px;height:48px;background:var(--brown);border-top:2px dashed #7b4222;color:#fff;text-align:center;font-size:7px;line-height:46px}
</style>
</head>
<body>
<div class="page">

  <header class="site-header">
    <div class="brand"><span class="brand-dot"></span>SunHaven</div>
    <nav class="main-nav script">
      <a class="current" href="#">Home</a>
      <a href="#">About us</a>
      <a href="#">Services</a>
      <a href="#">Patient Resources</a>
      <a href="#">FAQ</a>
      <a href="#">Contact Us</a>
    </nav>
  </header>

  <div class="hero" role="img" aria-label="Sunlit park with a family jumping together under trees"></div>

  <section class="hero-band">
    <svg class="band-arrow" style="left:52px" width="10" height="12" viewBox="0 0 10 12"><path d="M7 1 2 6l5 5" fill="none" stroke="#fff" stroke-width="2"/></svg>
    <div class="band-brand"><span class="brand-dot"></span>SunHaven</div>
    <p class="tagline script">We focus on providing care to mothers and families.</p>
    <a class="pay-btn script">Make a Payment</a>
    <svg class="band-arrow" style="left:654px" width="10" height="12" viewBox="0 0 10 12"><path d="M3 1l5 5-5 5" fill="none" stroke="#fff" stroke-width="2"/></svg>
  </section>

  <article class="card" style="left:60px">
    <h2 class="card-title script">Welcome to SunHaven</h2>
    <div class="card-photo" role="img" aria-label="Smiling multi-generation family" style="background:linear-gradient(90deg,#8fb0cc,#e6b494 40%,#e88aa0 70%,#c8d0da)"></div>
    <p class="card-text">Lorem Ipsum is simply dummy text of the printing and typesetting industry. Lorem Ipsum has been the industry's standard dummy text ever since the 1500s, when an unknown printer took a galley of type and scrambled it to make a type specimen book. It has survived not only five centuries, but also the leap into electronic typesetting .</p>
  </article>

  <article class="card" style="left:265px">
    <h2 class="card-title script">Why Choose Us ?</h2>
    <div class="card-photo" role="img" aria-label="Caregiver talking with an elderly woman" style="background:linear-gradient(90deg,#d6cfc4,#3ba0b8 40%,#e6d6c8 65%,#5c8fc0)"></div>
    <p class="card-text">Lorem Ipsum is simply dummy text of the printing and typesetting industry. Lorem Ipsum has been the industry's standard dummy text ever since the 1500s, when an unknown printer took a galley of type and scrambled it to make a type specimen book. It has survived not only five centuries, but also the leap into electronic typesetting .</p>
  </article>

  <article class="card" style="left:470px">
    <h2 class="card-title script">Latest News</h2>
    <div class="news-item">
      <div class="news-photo" role="img" aria-label="Hands forming a heart around a newborn" style="background:linear-gradient(135deg,#f1dccb,#d9a887)"></div>
      <p class="news-text"><b>Lorem Ipsum is simply dummy text of the printing and typesetting industry.</b> Lorem Ipsum has been the industry's standard dummy text ever into electronic typesetting .</p>
    </div>
    <a class="more-btn script">Read More</a>
    <div class="news-item" style="padding-top:14px">
      <div class="news-photo" role="img" aria-label="Doctor consulting with a patient" style="background:linear-gradient(135deg,#b89a80,#e8ecee 55%,#6e8a9c)"></div>
      <p class="news-text"><b>Lorem Ipsum is simply dummy text of the printing and typesetting industry.</b> Lorem Ipsum has been the industry's standard dummy text ever into electronic typesetting .</p>
    </div>
    <a class="more-btn script" style="margin-top:14px">Read More</a>
  </article>

  <h2 class="section-title script" style="left:60px;top:704px">Patient Resources</h2>
  <div class="rule" style="left:60px;top:724px;width:286px"></div>
  <div class="resource-photo" role="img" aria-label="Two hands reaching out to hold each other"></div>
  <p class="resource-text">Lorem Ipsum is simply dummy text of the printing and typesetting industry. Lorem Ipsum has been the industry's standard dummy text ever since the 1500s, when an unknown printer took a galley of type and scrambled it to make a type specimen book. It has survived not only five centuries remaining essentially unchanged.</p>

  <h2 class="section-title script" style="left:361px;top:704px">Our Services</h2>
  <div class="rule" style="left:361px;top:724px;width:290px"></div>

  <div class="service" style="top:740px">
    <div class="service-icon">
      <svg width="48" height="48" viewBox="0 0 48 48"><path d="M24 27c-6-4-9-7-9-10a4.5 4.5 0 0 1 9-1 4.5 4.5 0 0 1 9 1c0 3-3 6-9 10z" fill="#fff"/><path d="M10 26c2 6 6 10 14 10s12-4 14-10" fill="none" stroke="#fff" stroke-width="3" stroke-linecap="round"/></svg>
    </div>
    <div class="service-body">
      <h3 class="service-title script">Neque porro quisquam</h3>
      <p class="service-text">Sed ut perspiciatis unde omnis iste natus error sit voluptatem laudantium, totam rem aperiam, eaque ipsa sunt explicabo. totam rem illo inventore veritatis et quasi architecto beatae..</p>
    </div>
  </div>

  <div class="service" style="top:811px">
    <div class="service-icon">
      <svg width="48" height="48" viewBox="0 0 48 48" fill="#fff"><circle cx="16" cy="13" r="3.5"/><rect x="12" y="18" width="8" height="12" rx="2"/><rect x="13" y="29" width="2.5" height="9"/><rect x="16.5" y="29" width="2.5" height="9"/><circle cx="32" cy="13" r="3.5"/><path d="M27 18h10l3 13h-16z"/><rect x="29" y="30" width="2.5" height="8"/><rect x="32.5" y="30" width="2.5" height="8"/><circle cx="24" cy="23" r="2.5"/><rect x="22" y="26" width="4" height="9" rx="1"/></svg>
    </div>
    <div class="service-body">
      <h3 class="service-title script">Neque porro quisquam</h3>
      <p class="service-text">Sed ut perspiciatis unde omnis iste natus error sit voluptatem laudantium, totam rem aperiam, eaque ipsa sunt explicabo. totam rem illo inventore veritatis et quasi architecto beatae..</p>
    </div>
  </div>

  <h2 class="section-title script" style="left:347px;top:892px">Map</h2>
  <div class="rule" style="left:60px;top:918px;width:591px"></div>
  <div class="map" role="img" aria-label="Street map of the practice neighbourhood"></div>
  <aside class="contact-panel">
    <h3>Contact Us</h3>
    <p>Hollowbrook Office</p>
    <p>Linden Row 42</p>
    <p>20815 Eastfield</p>
    <p>Germany</p>
    <p class="gap">Telephone: +1 555 0142 877</p>
    <p>E-mail: hello@sunhaven.example</p>
  </aside>

  <footer class="site-footer script">Copyright © 2014 SunHaven. All rights reserved | Privacy Practices</footer>
</div>
</body>
</html>
```